Disposable food packaging business needs a product box design

We are looking for the design layout for our coffee cup cartons. They will be printed on white boxes and we would like them to be recognizable from a distance. These will not be seen by the customers buying coffee and the design is primarily for the Warehouse staff.
see attached a basic mockup and the type of cups that will be inside the cartons, creative freedom is still welcome, we are trying to achieve a more professional look.
Box size will be approximately 46cm wide, 50cm high and 38cm depth.
Things we would like.
- We would like our brand name 'KWT' to be one of the first things you notice. looking for a design for the brand/ logo.
-Each cup comes in multiple colours (black, white, rainbow, kraft (brown), we would like each box to have the colour of the cup incorporated into the design as well as the colour in writing. So that the colour of the cups is obvious.
-Each cup comes in multiple sizes (4oz, 6oz, 8oz, 8oz squat, 12oz and 16oz) that will need to be easily seen.
-A re-order code (example; RQB473).
-Carton quantity 1000 and inner sleeve qty 50.
-A barcode.
-Include attached symbols (eco friendly symbol to be black to match the rest).
So eventually there will be a total of 24 different coffee cup boxes- each with the same basic info.
-KWT brand
-Cup Colour (White, black, kraft and rainbow)
-Cup size (4, 6, 8, 8 squat, 12 and 16)
-Cup code (RQBxxx- xxx will be different for each cup/size)
-Carton qty 1000 sleeve qty 50 (same for every size and colour.
-Barcode (supplied later)
Initially just provide the generic design/ layout of one box- the successful designer will need to produce the design for all combinations.
NOTE - we are looking for the design of the outer carton for coffee cups. These cartons are for delivery of cups to cafes etc. They are not seen by the customer who purchases a coffee. The main requirement is for the warehouse staff to be able to easily identify and select the correct style and colour of cups.
Each carton contains 1000 cups.
Allow time for more entries.

```html
<!DOCTYPE html>
<html lang="en">
<head>
<meta charset="utf-8">
<title>KWT Coffee Cup Cartons – 12oz Range</title>
<link rel="stylesheet" href="https://fonts.googleapis.com/css2?family=Montserrat:wght@500;600;700;800&display=swap">
<style>
  :root {
    --page: #ffffff;
    --carton: #ececec;
    --carton-edge: #d9d9d9;
    --ink: #1d1d1d;
    --ink-soft: #3a3a3a;
    --black-band: #2a2a2a;
    --kraft-band: #c9a16a;
    --kraft-cup: #b98c55;
    --white-band: #f4f4f4;
    --white-cup: #f7f7f7;
    --mark: #6b4a2e;
    --label-text: #ffffff;
    --rainbow: linear-gradient(90deg, #e0306b 0%, #f08a2a 25%, #e6d23a 45%, #4fbf6a 65%, #3d7fe0 85%, #8a4fd8 100%);
    --rainbow-v: linear-gradient(180deg, #e0306b 0%, #f08a2a 22%, #e6d23a 42%, #4fbf6a 62%, #3d7fe0 82%, #8a4fd8 100%);
  }

  * { box-sizing: border-box; margin: 0; padding: 0; }

  html, body {
    width: 1200px;
    height: 900px;
    overflow: hidden;
    background: var(--page);
    font-family: "Montserrat", Arial, sans-serif;
    color: var(--ink);
  }

  .range {
    position: absolute;
    top: 360px;
    left: 45px;
    display: flex;
    gap: 30px;
    list-style: none;
  }

  .carton {
    position: relative;
    width: 255px;
    height: 290px;
    background: var(--carton);
    border: 1px solid var(--carton-edge);
  }

  .brand-dot {
    position: absolute;
    top: 36px;
    left: 72px;
    width: 36px;
    height: 36px;
    border-radius: 50%;
    background: var(--mark);
  }

  .brand-name {
    position: absolute;
    top: 76px;
    left: 12px;
    width: 170px;
    text-align: center;
    font-size: 46px;
    font-weight: 800;
    line-height: 1;
    letter-spacing: 1px;
    color: var(--ink);
  }

  .brand-sub {
    position: absolute;
    top: 126px;
    left: 12px;
    width: 170px;
    text-align: center;
    font-size: 14px;
    font-weight: 700;
    color: var(--ink-soft);
  }

  .reorder-code {
    position: absolute;
    top: 170px;
    left: 14px;
    padding: 2px 8px;
    font-size: 13px;
    font-weight: 700;
    letter-spacing: 5px;
    color: var(--label-text);
    background: var(--black-band);
  }

  .cup {
    position: absolute;
    top: 160px;
    left: 126px;
    width: 44px;
    height: 62px;
    clip-path: polygon(0 0, 100% 0, 88% 100%, 12% 100%);
  }

  .features {
    position: absolute;
    top: 198px;
    left: 14px;
    width: 112px;
    height: 22px;
    display: flex;
    align-items: center;
    gap: 4px;
    padding: 0 4px;
    background: #ffffff;
    list-style: none;
  }

  .feature {
    display: flex;
    align-items: center;
    gap: 2px;
    font-size: 4.5px;
    font-weight: 600;
    color: var(--ink);
    white-space: nowrap;
  }

  .feature-icon {
    width: 8px;
    height: 8px;
    border-radius: 50%;
    background: var(--ink);
    flex: none;
  }

  .qty {
    position: absolute;
    top: 244px;
    left: 14px;
    font-size: 12.5px;
    font-weight: 700;
    color: var(--ink-soft);
  }

  .band {
    position: absolute;
    top: 0;
    right: 0;
    width: 58px;
    height: 100%;
    display: flex;
    align-items: center;
    justify-content: center;
  }

  .band-text {
    writing-mode: vertical-rl;
    font-size: 25px;
    font-weight: 800;
    letter-spacing: 1.5px;
    white-space: nowrap;
  }

  .carton--black .band { background: var(--black-band); }
  .carton--black .band-text { color: #ffffff; }
  .carton--black .cup { background: var(--black-band); }

  .carton--kraft .band { background: var(--kraft-band); }
  .carton--kraft .band-text { color: var(--ink); }
  .carton--kraft .reorder-code { background: var(--kraft-band); }
  .carton--kraft .cup { background: var(--kraft-cup); }

  .carton--white .band { background: var(--white-band); border-left: 1px solid var(--carton-edge); }
  .carton--white .band-text { color: var(--ink); }
  .carton--white .colour-word { color: transparent; -webkit-text-stroke: 1px var(--ink); }
  .carton--white .cup { background: var(--white-cup); border: 1px solid var(--carton-edge); }

  .carton--rainbow .band { background: var(--rainbow-v); }
  .carton--rainbow .band-text { color: #ffffff; }
  .carton--rainbow .reorder-code { background: var(--rainbow); }
  .carton--rainbow .cup { background: var(--rainbow-v); opacity: 0.85; }
</style>
</head>
<body>
<ul class="range">

  <li class="carton carton--black">
    <span class="brand-dot"></span>
    <h2 class="brand-name">KWT</h2>
    <p class="brand-sub">COFFE CUPS</p>
    <span class="reorder-code">RQB682</span>
    <span class="cup" role="img" aria-label="Black single wall 12oz paper cup"></span>
    <ul class="features">
      <li class="feature"><span class="feature-icon"></span>Leakproof</li>
      <li class="feature"><span class="feature-icon"></span>Compostable</li>
      <li class="feature"><span class="feature-icon"></span>Eco friendly</li>
    </ul>
    <p class="qty">QTY 1000 50X20</p>
    <div class="band"><span class="band-text">12oz <span class="colour-word">BLACK</span> S/W</span></div>
  </li>

  <li class="carton carton--kraft">
    <span class="brand-dot"></span>
    <h2 class="brand-name">KWT</h2>
    <p class="brand-sub">COFFE CUPS</p>
    <span class="reorder-code">RQB681</span>
    <span class="cup" role="img" aria-label="Kraft brown single wall 12oz paper cup"></span>
    <ul class="features">
      <li class="feature"><span class="feature-icon"></span>Leakproof</li>
      <li class="feature"><span class="feature-icon"></span>Compostable</li>
      <li class="feature"><span class="feature-icon"></span>Eco friendly</li>
    </ul>
    <p class="qty">QTY 1000 50X20</p>
    <div class="band"><span class="band-text">12oz <span class="colour-word">KRAFT</span> S/W</span></div>
  </li>

  <li class="carton carton--white">
    <span class="brand-dot"></span>
    <h2 class="brand-name">KWT</h2>
    <p class="brand-sub">COFFE CUPS</p>
    <span class="reorder-code">RQB680</span>
    <span class="cup" role="img" aria-label="White single wall 12oz paper cup"></span>
    <ul class="features">
      <li class="feature"><span class="feature-icon"></span>Leakproof</li>
      <li class="feature"><span class="feature-icon"></span>Compostable</li>
      <li class="feature"><span class="feature-icon"></span>Eco friendly</li>
    </ul>
    <p class="qty">QTY 1000 50X20</p>
    <div class="band"><span class="band-text">12oz <span class="colour-word">WHITE</span> S/W</span></div>
  </li>

  <li class="carton carton--rainbow">
    <span class="brand-dot"></span>
    <h2 class="brand-name">KWT</h2>
    <p class="brand-sub">COFFE CUPS</p>
    <span class="reorder-code">RQB683</span>
    <span class="cup" role="img" aria-label="Rainbow gradient single wall 12oz paper cup"></span>
    <ul class="features">
      <li class="feature"><span class="feature-icon"></span>Leakproof</li>
      <li class="feature"><span class="feature-icon"></span>Compostable</li>
      <li class="feature"><span class="feature-icon"></span>Eco friendly</li>
    </ul>
    <p class="qty">QTY 1000 50X20</p>
    <div class="band"><span class="band-text">12oz <span class="colour-word">RAINBOW</span> S/W</span></div>
  </li>

</ul>
</body>
</html>
```